Company or website name
- www.tapwellHOMEfind.com
- Links to the website
- tapwellhomefind.com
- Describe your company and organization and target audience
- My name is calvin brisk from houston texas. I am a realtor. I have been trying very hard to develop a site that not only reflects me but can generate some business. I have a site with an idx search but it is too expensive and I really dont think IDX is the way to go. I just want a site that is neat and holds people interest. For this contest, I pretty much did all the work. I need your creativity. I have a drop box link that has everything in it. Each section is marked. I have about me, about what I do, How i am different, Neighborhoods i specialize in etc.
- The design should have the following
- I want in my site the following: I would Live Feed of my Snapvane and Friendloop page on the first main page I want my video playing as the main shot. I have 2 give a ways (something of value), buyers handbook and sellers handbook I do a monthly newsletter i would also like to give some attention to. I want a chat box that is either a bot or goes into text message to me www.tapwellHOMEfind.com is the website url dropbox link: https://www.boxlockerhub.com/sh/7kqp2n48vtzz15r/BBLmr_3pH27hkwQTqN9dYfLtB?dl=0 If you can use the idx's that my assocation provides that would be great. I have been told they are frames, it is ok if you dont but if you can they do have some great info.

```html
<!DOCTYPE html>
<html lang="en">
<head>
<meta charset="utf-8">
<title>tapwellHOMEfind – Calvin Brisk, Houston Realtor</title>
<link href="https://fonts.googleapis.com/css2?family=Jost:wght@300;400;500&family=Arimo:ital,wght@0,400;1,400&display=swap" rel="stylesheet">
<style>
:root{
  --red:#d40d12;
  --orange:#f2a100;
  --ink:#333;
  --muted:#8a8a8a;
  --panel:#f2f2f2;
  --line:#dedede;
  --white:#fff;
}
*{box-sizing:border-box;margin:0;padding:0}
html,body{width:1200px;height:2760px;overflow:hidden;background:var(--white)}
body{position:relative;font-family:'Jost',sans-serif;color:var(--ink)}
.abs{position:absolute}
.topbar{left:0;top:0;width:1200px;height:28px;background:var(--red);color:#fff;font-size:11px}
.topbar .auth{left:126px;top:7px;display:flex;gap:28px}
.topbar .social{right:142px;top:7px;display:flex;gap:18px;font-size:10px}
.header{left:0;top:28px;width:1200px;height:48px}
.logo{left:144px;top:16px;font-size:14px;font-weight:500;color:var(--ink);display:flex;align-items:center;gap:6px}
.logo .dot{width:10px;height:10px;background:var(--red)}
.logo small{position:absolute;top:18px;left:20px;font-size:6px;color:var(--muted);white-space:nowrap}
.contact{top:12px;font-size:10px;line-height:13px;color:var(--ink)}
.contact span{display:block;font-size:8px;color:var(--muted)}
.nav{left:0;top:76px;width:1200px;height:38px;background:#f4f4f4;border-bottom:1px solid var(--line)}
.nav ul{position:absolute;left:359px;top:0;display:flex;list-style:none;height:38px}
.nav li{font-size:9px;color:var(--muted);display:flex;align-items:center;justify-content:center;border-right:1px solid var(--line);height:38px}
.nav li.active{background:#fff;color:var(--orange);border-left:1px solid var(--line)}
.dropdown{left:854px;top:114px;width:123px;background:#f4f4f4;font-size:8px;color:var(--muted)}
.dropdown div{height:22px;line-height:22px;text-align:center;border-bottom:1px solid var(--line)}
.hero{left:0;top:114px;width:1200px;height:594px;background:linear-gradient(180deg,#c9ccd1 0%,#b7b8b4 25%,#6aa9c9 45%,#3e86b3 62%,#d4d4d0 85%,#a8a8a4 100%)}
.play{left:552px;top:325px;width:96px;height:96px;border-radius:50%;background:rgba(255,255,255,.55);border:3px solid rgba(255,255,255,.8)}
.searchpanel{left:127px;top:585px;width:949px;height:123px;background:rgba(255,255,255,.35)}
.searchbox{left:172px;top:627px;width:856px;height:52px;background:#fff;border-radius:4px;font-size:15px;color:#666;padding:16px 38px;font-weight:300}
.submit{left:874px;top:627px;width:154px;height:52px;background:var(--red);color:var(--orange);font-size:14px;text-align:center;line-height:52px;border-radius:0 4px 4px 0}
.redhead{background:var(--red);color:#fff;height:60px;line-height:60px;font-weight:300}
.quick{left:127px;top:762px;width:361px;height:541px;background:var(--panel)}
.quick .redhead{text-align:center;font-size:17px}
.avatar{left:117px;top:78px;width:127px;height:127px;border-radius:50%;background:radial-gradient(circle at 50% 40%,#c9a894 0%,#7c6c66 55%,#34343a 100%)}
.agent{left:0;top:218px;width:361px;text-align:center}
.agent h2{font-size:29px;font-weight:400;color:#444}
.agent p{font-size:15px;color:var(--red);line-height:19px;margin-top:10px}
.field{background:#fff;font-size:9px;color:#aaa;padding:8px 9px}
.cta{left:83px;top:482px;width:213px;height:42px;background:var(--red);color:var(--orange);text-align:center;line-height:42px;font-size:15px}
.recent-head{left:509px;top:762px;width:567px;height:60px;background:var(--panel)}
.recent-head .redhead{position:absolute;left:0;top:0;width:195px;text-align:center;font-size:22px}
.viewmore{right:11px;top:21px;width:149px;height:21px;background:var(--red);color:var(--orange);font-size:8px;line-height:21px;padding-left:12px}
.card{background:var(--panel)}
.card .img{position:absolute;left:0;top:0;width:100%;height:180px}
.card .desc{position:absolute;left:19px;top:194px;width:236px;font-size:8px;line-height:11.3px;color:#888}
.meta{font-size:10px;color:#666}
.meta b{font-weight:400;color:var(--red)}
.more{font-size:10px;color:var(--red);text-decoration:underline;font-style:italic}
.feat-head{left:127px;top:1349px;width:949px;height:59px;background:var(--panel)}
.feat-head .redhead{position:absolute;left:0;top:0;width:228px;height:59px;line-height:59px;text-align:center;font-size:23px}
.arrowbtn{top:18px;width:25px;height:21px;background:#666}
.fcard{top:1431px;height:362px;background:var(--panel)}
.fcard .img{position:absolute;left:0;top:0;width:100%;height:217px}
.fcard .body{position:absolute;left:27px;top:226px;font-family:'Arimo',sans-serif}
.fcard h3{font-family:'Jost',sans-serif;font-weight:400;font-size:14px;color:var(--orange)}
.fcard .addr{font-size:8px;font-style:italic;color:#666;margin-top:6px}
.fcard .loc{font-size:7px;font-style:italic;color:#888;margin-top:6px;display:flex;gap:4px;align-items:center}
.fcard .zip{font-size:7px;font-style:italic;color:#999;margin-top:20px}
.fcard .price{display:inline-block;margin-top:16px;background:#777;color:#fff;font-size:7px;padding:5px 8px}
.viewdetail{left:64px;top:84px;width:152px;height:48px;border:2px solid var(--orange);color:var(--orange);text-align:center;line-height:44px;font-size:13px}
.analysis{left:0;top:1848px;width:1200px;height:411px;background:var(--panel)}
.tabs{left:206px;top:1904px;width:809px;height:26px;border-bottom:3px solid #dcdcdc;display:flex;font-family:'Arimo',sans-serif;font-size:14px;color:#c4c4c4}
.tabs div{text-align:center}
.tabs .on{color:var(--orange);border-bottom:3px solid var(--orange);margin-bottom:-3px}
.trend{left:240px;top:1990px;font-family:'Arimo',sans-serif}
.trend h4{font-weight:400;font-size:14px;color:#c4c4c4;line-height:17px}
.trend h4 span{display:block;color:var(--orange)}
.trend p{margin-top:23px;font-size:10px;color:#c4c4c4;line-height:14px;width:270px;margin-left:-3px}
.outline{left:235px;top:2124px;width:180px;height:48px;border:2px solid var(--orange);color:var(--orange);font-family:'Arimo',sans-serif;font-size:13px;text-align:center;line-height:44px}
.chart{left:560px;top:1978px;width:406px;height:207px;background:#fff}
.communities{left:0;top:2314px;width:1200px;height:269px;background:linear-gradient(135deg,#4a2a1c 0%,#7a3d22 35%,#5b3020 60%,#3a2418 100%)}
.communities h2{position:absolute;left:0;top:62px;width:1200px;text-align:center;font-size:37px;font-weight:400;color:var(--orange)}
.communities p{position:absolute;left:0;top:110px;width:1200px;text-align:center;font-size:13px;color:#f3e6dc;font-weight:300}
.area{top:176px;height:22px;border-bottom:2px solid var(--orange);color:var(--orange);font-family:'Arimo',sans-serif;font-size:12px;text-align:center}
.footer{left:0;top:2637px;width:1200px;height:123px;background:var(--red);color:#fff;font-family:'Arimo',sans-serif}
.footer .links{position:absolute;left:127px;top:44px;display:flex;font-size:10px}
.footer .links span{padding:0 34px 0 0;margin-right:34px;border-right:1px solid #fff;height:18px;line-height:18px}
.footer .links span:first-child{padding-right:36px}
.footer .links span:last-child{border:none}
.footer .copy{position:absolute;left:127px;top:85px;font-size:8px}
.footer .search{position:absolute;left:913px;top:42px;width:160px;height:18px;border-bottom:1px solid #fff}
.footer .soc{position:absolute;top:70px;display:flex;gap:6px;left:976px;font-size:7px;font-family:'Jost',sans-serif}
.footer .soc span{display:flex;align-items:center;gap:3px}
.footer .soc i{display:inline-block;width:12px;height:12px;border:1.5px solid #fff;border-radius:50%}
</style>
</head>
<body>

<div class="abs topbar">
  <div class="abs auth"><span>→ Login</span><span>✔ Register</span></div>
  <div class="abs social"><span>Snapvane</span><span>Friendloop</span><span>Chirpnest</span></div>
</div>

<header class="abs header">
  <div class="abs logo"><i class="dot"></i>www.tapwellHOMEfind.com<small>Calvin, Your Favorite Realtor</small></div>
  <div class="abs contact" style="left:705px"><span>Free Line For You</span>+60-101-555-47</div>
  <div class="abs contact" style="left:851px"><span>Email Us</span>cs@tapwellhomefind.com</div>
  <div class="abs contact" style="left:990px"><span>Working Hours</span>09:00 to 17:00</div>
</header>

<nav class="abs nav">
  <ul>
    <li class="active" style="width:79px">Home</li>
    <li style="width:86px">Search</li>
    <li style="width:78px">Sell</li>
    <li style="width:120px">Communities</li>
    <li style="width:133px">Market Insider</li>
    <li style="width:123px">Resources ▾</li>
    <li style="width:104px">About</li>
  </ul>
</nav>

<div class="abs hero" role="img" aria-label="Video still: infinity pool on a hillside terrace overlooking the city"></div>
<div class="abs play"><svg width="90" height="90" viewBox="0 0 90 90"><polygon points="32,45 61,27 61,63" fill="#1b6ea8"/></svg></div>
<div class="abs searchpanel"></div>
<div class="abs searchbox">Search for Location or Listing</div>
<div class="abs submit">SUBMITE</div>

<div class="abs dropdown"><div>Blog</div><div>Finance</div><div>Partners</div><div>Careers</div></div>

<section class="abs quick">
  <div class="redhead">QUICK CONTACT FORM</div>
  <div class="abs avatar" role="img" aria-label="Portrait photo of Calvin Brisk"></div>
  <div class="abs agent"><h2>Calvin Brisk</h2><p>CNE, Luxury, CPRES<br>Brightpath Memorial</p></div>
  <div class="abs field" style="left:16px;top:324px;width:163px;height:28px">Name*</div>
  <div class="abs field" style="left:16px;top:379px;width:163px;height:28px">Email*</div>
  <div class="abs field" style="left:16px;top:429px;width:163px;height:28px">Phone</div>
  <div class="abs field" style="left:207px;top:324px;width:140px;height:83px">Message</div>
  <div class="abs field" style="left:207px;top:429px;width:140px;height:28px;font-size:6px;display:flex;justify-content:space-between;align-items:center"><span>☐ Not a robot</span><span>VerifyBox</span></div>
  <div class="abs cta">CONTACT ME</div>
</section>

<div class="abs recent-head">
  <div class="redhead">Recently Listed</div>
  <div class="abs viewmore">View more properties ⟶</div>
</div>

<article class="abs card" style="left:509px;top:844px;width:273px;height:459px">
  <div class="img" role="img" aria-label="Renaissance-style mansion with fountain at dusk" style="background:linear-gradient(180deg,#5c6fa8 0%,#c9a36a 50%,#3f5a3a 100%)"></div>
  <p class="desc">This elegant home with multi-tiered gardens, fountains and terraces sits on a corner lot in a guarded and gated luxury community with classic design features created by master craftsmen, where old-world charm blends with modern living. Designed for entertaining on a grand scale, the first floor interiors open to over 150 linear feet of gallery porches across the rear that step down to the pool level. All bedrooms have outdoor balconies and the private master suite is enviably luxurious.</p>
  <div class="abs meta" style="left:19px;top:356px">Status &nbsp;&nbsp;&nbsp;&nbsp;&nbsp;: &nbsp;<b>ACTIVE</b></div>
  <div class="abs meta" style="left:19px;top:382px">Price &nbsp;&nbsp;&nbsp;&nbsp;&nbsp;&nbsp;&nbsp;: &nbsp;<b>$12,000,000</b></div>
  <div class="abs meta" style="left:19px;top:404px">Location &nbsp;: <span style="font-size:6px;color:#aaa;font-style:italic;display:inline-block;vertical-align:top;line-height:8px">4417 Saddlebrook Lane<br>Houston, TX 77024</span></div>
  <div class="abs more" style="left:193px;top:423px">more details</div>
</article>

<article class="abs card" style="left:802px;top:844px;width:272px;height:459px">
  <div class="img" role="img" aria-label="Aerial view of a cleared land parcel" style="background:linear-gradient(160deg,#a89478 0%,#cbb89a 50%,#8b7a62 100%)"></div>
  <p class="desc">This elegant home with multi-tiered gardens, fountains and terraces sits on a corner lot in a guarded and gated luxury community with classic design features created by master craftsmen, where old-world charm blends with modern living. Designed for entertaining on a grand scale, the first floor interiors open to over 150 linear feet of gallery porches across the rear that step down to the pool level. All bedrooms have outdoor balconies and the private master suite is enviably luxurious.</p>
  <div class="abs meta" style="left:17px;top:356px">Status &nbsp;&nbsp;&nbsp;&nbsp;&nbsp;: &nbsp;<b>ACTIVE</b></div>
  <div class="abs meta" style="left:17px;top:382px">Price &nbsp;&nbsp;&nbsp;&nbsp;&nbsp;&nbsp;&nbsp;: &nbsp;<b>$50,000,000</b></div>
  <div class="abs meta" style="left:17px;top:404px">Location &nbsp;: <span style="font-size:6px;color:#aaa;font-style:italic;display:inline-block;vertical-align:top;line-height:8px">Wexford Parkway, Katy<br>TX 77493</span></div>
  <div class="abs more" style="left:191px;top:423px">more details</div>
</article>

<div class="abs feat-head">
  <div class="redhead">Featured Listings</div>
  <div class="abs arrowbtn" style="left:842px"><svg width="25" height="21"><polyline points="15,6 10,10.5 15,15" fill="none" stroke="#fff" stroke-width="2"/></svg></div>
  <div class="abs arrowbtn" style="left:900px"><svg width="25" height="21"><polyline points="10,6 15,10.5 10,15" fill="none" stroke="#fff" stroke-width="2"/></svg></div>
</div>

<article class="abs fcard" style="left:127px;width:289px">
  <div class="img" role="img" aria-label="Dusk street scene with parked cars" style="background:linear-gradient(180deg,#4c5560 0%,#2b2f33 60%,#1c1d1f 100%)"></div>
  <div class="abs viewdetail">VIEW DETAIL</div>
  <div class="body"><h3>Listing</h3><div class="addr">HOUSTON - 1420 LANTERNWOOD STREET</div>
  <div class="loc"><svg width="7" height="9" viewBox="0 0 7 9"><path d="M3.5 0a3.3 3.3 0 0 0-3.3 3.3C.2 5.8 3.5 9 3.5 9s3.3-3.2 3.3-5.7A3.3 3.3 0 0 0 3.5 0z" fill="#555"/></svg>United States - Harris</div>
  <div class="zip">Zip : 77093</div><div class="price">$799,000</div></div>
</article>

<article class="abs fcard" style="left:456px;width:291px">
  <div class="img" role="img" aria-label="Brick ranch house with green lawn and trees" style="background:linear-gradient(180deg,#5f8f3a 0%,#8a6a4a 45%,#6fa43a 100%)"></div>
  <div class="body"><h3>Houston, TX</h3><div class="addr">HOUSTON - 1420 LANTERNWOOD STREET</div>
  <div class="loc"><svg width="7" height="9" viewBox="0 0 7 9"><path d="M3.5 0a3.3 3.3 0 0 0-3.3 3.3C.2 5.8 3.5 9 3.5 9s3.3-3.2 3.3-5.7A3.3 3.3 0 0 0 3.5 0z" fill="#555"/></svg>United States - Harris</div>
  <div class="zip">Zip : 77093</div><div class="price">$399,990</div></div>
</article>

<article class="abs fcard" style="left:786px;width:290px">
  <div class="img" role="img" aria-label="Backyard garden with stone fire pit and house" style="background:linear-gradient(180deg,#3f6a2e 0%,#6b8f3e 45%,#6a4c3a 100%)"></div>
  <div class="body"><h3>Houston, TX</h3><div class="addr">HOUSTON - 1420 LANTERNWOOD STREET</div>
  <div class="loc"><svg width="7" height="9" viewBox="0 0 7 9"><path d="M3.5 0a3.3 3.3 0 0 0-3.3 3.3C.2 5.8 3.5 9 3.5 9s3.3-3.2 3.3-5.7A3.3 3.3 0 0 0 3.5 0z" fill="#555"/></svg>United States - Harris</div>
  <div class="zip">Zip : 77093</div><div class="price">$399,990</div></div>
</article>

<section class="abs analysis"></section>
<div class="abs tabs">
  <div class="on" style="width:220px">MARKET ANALYSIS</div>
  <div style="width:190px">COMUNITY INFO</div>
  <div style="width:160px">LOCAL SCHOOLS</div>
  <div style="width:239px">INSIDERS TIPS</div>
</div>
<div class="abs trend">
  <h4>HOUSING MARKET TRENDS<span>SOLD &nbsp;VS LISTED</span></h4>
  <p>Understand the difference between "listing prices" (what sellers are asking for) and "sold prices" (what buyers are willing to pay).</p>
</div>
<div class="abs outline">VIEW ALL ANALYSIS</div>

<div class="abs chart">
  <svg width="406" height="207" viewBox="0 0 406 207" font-family="Arimo, sans-serif" font-size="6" fill="#666">
    <g stroke="#e2e2e2" stroke-width="1">
      <line x1="42" y1="14" x2="380" y2="14"/><line x1="42" y1="31" x2="380" y2="31"/><line x1="42" y1="48" x2="380" y2="48"/><line x1="42" y1="66" x2="380" y2="66"/><line x1="42" y1="83" x2="380" y2="83"/><line x1="42" y1="101" x2="380" y2="101"/><line x1="42" y1="118" x2="380" y2="118"/><line x1="42" y1="136" x2="380" y2="136"/><line x1="42" y1="153" x2="380" y2="153"/><line x1="42" y1="170" x2="380" y2="170"/>
    </g>
    <line x1="42" y1="14" x2="42" y2="170" stroke="#999"/>
    <line x1="42" y1="170" x2="380" y2="170" stroke="#999"/>
    <g text-anchor="end">
      <text x="39" y="16">$397k</text><text x="39" y="33">$388k</text><text x="39" y="50">$376k</text><text x="39" y="68">$365k</text><text x="39" y="85">$354k</text><text x="39" y="103">$344k</text><text x="39" y="120">$333k</text><text x="39" y="138">$323k</text><text x="39" y="155">$312k</text><text x="39" y="172">$301k</text>
    </g>
    <g text-anchor="middle">
      <text x="42" y="180">10/1</text><text x="73" y="180">11/1</text><text x="104" y="180">12/1</text><text x="134" y="180">1/1</text><text x="165" y="180">2/1</text><text x="196" y="180">3/1</text><text x="226" y="180">4/1</text><text x="257" y="180">5/1</text><text x="288" y="180">6/1</text><text x="318" y="180">7/1</text><text x="349" y="180">8/1</text><text x="380" y="180">9/1</text>
    </g>
    <polyline fill="none" stroke="#1f78c8" stroke-width="1.6" points="42,55 60,57 73,61 90,50 104,50 120,48 134,46 150,40 165,40 180,37 196,34 215,32 235,30 257,31 275,29 300,28 318,30 335,30 355,32 370,44 380,58"/>
    <polyline fill="none" stroke="#5cc85c" stroke-width="1.6" points="42,97 55,125 73,148 90,140 104,137 125,136 140,78 150,75 165,70 180,120 196,153 212,120 222,77 235,125 250,78 260,130 270,148 283,143 298,78 310,73 325,90 340,88 355,83 372,73 380,66"/>
    <rect x="131" y="188" width="6" height="6" fill="#1f78c8"/><text x="140" y="193">Median Listing Price</text>
    <rect x="207" y="188" width="6" height="6" fill="#5cc85c"/><text x="216" y="193">Median Sold Price</text>
  </svg>
</div>

<section class="abs communities" role="img" aria-label="Tree-lined neighborhood street in autumn tones">
  <h2>COMMUNITIES SERVED</h2>
  <p>Proudly serving the following communities:</p>
  <div class="abs area" style="left:150px;width:122px">BELLAIRE AREA</div>
  <div class="abs area" style="left:402px;width:149px">MEYERLAND AREA</div>
  <div class="abs area" style="left:660px;width:150px">MUSEUM DISTRICT</div>
  <div class="abs area" style="left:906px;width:148px">UNIVERSYTI AREA</div>
</section>

<footer class="abs footer">
  <div class="links"><span>Brightpath Memorial</span><span>Terms of Use</span><span>Privacy Policy</span><span>Contact Us</span></div>
  <div class="copy">© 2019 Brightpath Memorial. All Rights Reserved</div>
  <div class="search"><svg style="position:absolute;right:4px;top:2px" width="10" height="10" viewBox="0 0 10 10"><circle cx="4" cy="4" r="3" fill="none" stroke="#fff" stroke-width="1.4"/><line x1="6.2" y1="6.2" x2="9.5" y2="9.5" stroke="#fff" stroke-width="1.4"/></svg></div>
  <div class="soc"><span><i></i>Friendloop</span><span><i></i>Snapvane</span><span><i></i>Reeltube</span></div>
</footer>

</body>
</html>
```